Flyer for annual LUMEN SUMMIT 2020

I would like a church event flyer designed. The event is called "LUMEN SUMMIT 2020". I am looking for a professional, yet catchy design that uses our brand colors and logo creatively while communicating key information of the event effectively.

1. The logo is attached in two color formats. The designer has the choice to use them as he/she want.

2. The location of the event is: Talbot Community Center, 482 Wexley Street, Portland, ME 04107

3. Time and date of event. The designer can organize and format the date and time as he/she pleases.
Thursday December 31st @ 6:30PM
Friday January 1st @ 6:30PM
Saturday 2nd @ 6:30PM
Sunday 3rd @ 4:30PM

4. The topic of the event is "Deep Wells and Tall Cedars". The designer is free to use this phrase as he/she pleases to create a good composition.

5. Speaker: Prophet Marcus Obuya (2 pictures of the speaker to choose from are attached)

6. Contact information: contact@harborvine.org - Telephone number: 207 583 2194

7. I would also like the following three words on the flyer. These words describe the focus of the event: FIRE, REVIVAL, PROPHETIC

Target Market(s)

Young adults

Font styles to use
Sans Serif

Requirements
Must have
• Logo, speaker's picture
Should not have
• cross image, church image

```html
<!DOCTYPE html>
<html lang="en">
<head>
<meta charset="utf-8">
<title>Lumen Summit 2020 Flyer</title>
<link rel="stylesheet" href="https://fonts.googleapis.com/css2?family=Cinzel:wght@500;600;700&display=swap">
<style>
  :root {
    --navy: #0d2c4f;
    --orange: #e88a1a;
    --paper: #f7f7f7;
    --backdrop: #dcdcdc;
    --white: #ffffff;
  }
  * { margin: 0; padding: 0; box-sizing: border-box; }
  html, body { width: 1070px; height: 1200px; overflow: hidden; }
  body {
    background: var(--backdrop);
    font-family: "Cinzel", "Times New Roman", serif;
    position: relative;
  }
  .flyer {
    position: absolute;
    left: 122px; top: 14px;
    width: 826px; height: 1172px;
    background: var(--paper);
    overflow: hidden;
  }
  .flyer > * { position: absolute; }
  .line { line-height: 1; white-space: nowrap; }

  .navy-field { left: 0; top: 505px; width: 826px; height: 539px; background: var(--navy); }
  .contact-bar { left: 0; top: 1044px; width: 826px; height: 50px; background: var(--orange); }

  .title { left: 56px; top: 82px; color: var(--navy); font-weight: 700; font-size: 62px; letter-spacing: 1px; }
  .title span { display: block; line-height: 62px; }
  .title .year { color: var(--orange); font-weight: 600; font-size: 70px; line-height: 72px; margin-top: 4px; }

  .brand {
    left: 518px; top: 118px;
    color: var(--navy); font-weight: 600; font-size: 66px; line-height: 1;
    letter-spacing: 1px;
  }

  .pin { left: 52px; top: 324px; width: 32px; height: 40px; }
  .address { left: 103px; top: 315px; color: var(--navy); font-weight: 600; font-size: 23px; line-height: 27.5px; }

  .schedule {
    left: 53px; top: 435px; width: 715px; height: 139px;
    background: var(--orange); border-radius: 14px;
    display: grid; grid-template-columns: repeat(4, 1fr);
    color: var(--white);
  }
  .schedule .rule { position: absolute; left: 15px; right: 20px; top: 60px; height: 2px; background: rgba(255,255,255,0.85); }
  .day { position: relative; text-align: center; }
  .day + .day::before { content: ""; position: absolute; left: 0; top: 15px; bottom: 12px; width: 2px; background: rgba(255,255,255,0.85); }
  .day .date { display: block; margin-top: 22px; font-size: 21px; font-weight: 500; }
  .day .weekday { display: block; margin-top: 24px; font-size: 18px; font-weight: 600; }
  .day .time { display: block; margin-top: 2px; font-size: 14px; }

  .speaker-photo {
    left: 82px; top: 647px; width: 336px; height: 336px; border-radius: 50%;
    border: 3px solid var(--white);
    padding: 6px; background: var(--navy);
  }
  .speaker-photo .fill {
    width: 100%; height: 100%; border-radius: 50%;
    background: radial-gradient(circle at 50% 35%, #5c4a40 0%, #8a7b6e 45%, #b8412a 80%, #a8361f 100%);
  }

  .label { color: var(--white); font-weight: 500; font-size: 33px; }
  .label-rule { height: 2px; background: var(--white); }
  .accent { color: var(--orange); font-weight: 600; font-size: 36px; line-height: 45px; }

  .speaker-label { left: 468px; top: 668px; }
  .speaker-rule { left: 638px; top: 678px; width: 107px; }
  .speaker-name { left: 468px; top: 706px; }

  .topic-label { left: 468px; top: 845px; }
  .topic-rule { left: 596px; top: 856px; width: 149px; }
  .topic-name { left: 468px; top: 883px; }

  .contact { left: 41px; top: 1060px; color: var(--navy); font-weight: 600; font-size: 22px; }
  .focus { left: 0; width: 826px; top: 1119px; text-align: center; color: var(--orange); font-weight: 600; font-size: 36px; letter-spacing: 1px; }
</style>
</head>
<body>
  <main class="flyer">
    <div class="navy-field"></div>
    <div class="contact-bar"></div>

    <h1 class="title">
      <span>Lumen</span>
      <span>Summit</span>
      <span class="year">2020</span>
    </h1>

    <div class="brand line">HALVEN</div>

    <svg class="pin" viewBox="0 0 32 40" aria-hidden="true">
      <path d="M16 0C7.2 0 0 7 0 15.6 0 27 16 40 16 40s16-13 16-24.4C32 7 24.8 0 16 0z" fill="var(--orange)"/>
      <circle cx="16" cy="15" r="6" fill="var(--paper)"/>
    </svg>
    <address class="address" style="font-style:normal">
      Talbot Community Center,<br>
      482 Wexley Street, Portland,<br>
      ME 04107
    </address>

    <section class="schedule">
      <div class="rule"></div>
      <div class="day"><span class="date">DEC 31ST</span><span class="weekday">Thursday</span><span class="time">@ 6:30PM</span></div>
      <div class="day"><span class="date">JAN 1ST</span><span class="weekday">FRIDAY</span><span class="time">@ 6:30PM</span></div>
      <div class="day"><span class="date">JAN 2ND</span><span class="weekday">SATURDAY</span><span class="time">@ 6:30PM</span></div>
      <div class="day"><span class="date">JAN 3RD</span><span class="weekday">SUNDAY</span><span class="time">@ 4:30PM</span></div>
    </section>

    <div class="speaker-photo"><div class="fill" role="img" aria-label="Portrait photo of the speaker, Prophet Marcus Obuya"></div></div>

    <div class="label speaker-label line">SPEAKER</div>
    <div class="label-rule speaker-rule"></div>
    <div class="accent speaker-name">Prophet<br>Marcus Obuya</div>

    <div class="label topic-label line">TOPIC</div>
    <div class="label-rule topic-rule"></div>
    <div class="accent topic-name">Deep Wells<br>And Tall Cedars</div>

    <div class="contact line">contact@harborvine.org - Telephone : 207 583 2194</div>
    <div class="focus line">FIRE, REVIVAL, PROPHETIC</div>
  </main>
</body>
</html>
```